Flyer Design for Private Tuition

Kestrel Tuition (www.KestrelTuition-example.co.uk) is an after school/ weekend tutoring service for students aged 4-18 years olds. Please look at our website for further information about our features and benefits. However something I think may be good to add is: Money back guarantee, Free trial, Free assessment. I would like it to include a £25 voucher symbol.

I have uploaded the following:
- Tamsford Bank logo for the colour I want (Light Blue with white)

Please also look at our website: www.KestrelTuition-example.com

Please contact me for any further info. Good luck!

Target Market(s)

Parents of children aged 4-18 years old.

Industry/Entity Type

Education

Colors
85cae6
ffffff

Requirements
Must have
• My logo should be LIGHT BLUE logo colours of like these companies:
• http://www.tamsford-example.co.uk
• https://www.vornalex-example.com
• Background should be white.
• Must be a clean, fresh look and feel.
Nice to have
• A nice Kestrel Tuition logo
• An image of an A* ..... or maybe an A* graded on a piece of work.... or maybe some kind of award/ achievement or something like that. This would signify the feeling of success to the target market (parents).
Should not have
• Due to religious reasons I do not want any pictures of human/animal faces. Blurred out faces or parts of bodies are ok, (Perhaps you could use images of an A* Grade? Success/ Achievement? Graduation hat? Stationary?)
• Please do not include the ZPD Education logo (this is the parent company but it will be confusing to include it).

```html
<!DOCTYPE html>
<html lang="en">
<head>
<meta charset="utf-8">
<title>Kestrel Tuition Flyer</title>
<link href="https://fonts.googleapis.com/css2?family=Montserrat:wght@700&family=Raleway:wght@400;500;800&display=swap" rel="stylesheet">
<style>
  :root{
    --navy:#0a2233;
    --hero-blue:#5aa6cf;
    --bright-blue:#1aa9dc;
    --heading-navy:#0d3a58;
    --section-navy:#0d4a6e;
    --footer-navy:#0a4a6c;
    --body-dark:#1a2a35;
    --body-grey:#8a8a8a;
    --white:#ffffff;
    --icon-blue:#4fb7e3;
    --stage:#e6e6e6;
  }
  html,body{margin:0;padding:0;width:1200px;height:1200px;overflow:hidden;background:var(--stage);}
  .flyer{
    position:absolute;left:196px;top:30px;width:985px;height:1390px;
    transform:scale(0.82);transform-origin:top left;
    background:var(--white);overflow:hidden;
    font-family:"Raleway",sans-serif;
  }
  .flyer-shapes{position:absolute;inset:0;width:985px;height:1390px;}
  .brand{
    position:absolute;left:690px;top:78px;display:flex;align-items:center;gap:14px;
    font-family:"Raleway",sans-serif;font-weight:800;font-size:38px;line-height:1;
    color:var(--bright-blue);letter-spacing:1px;
  }
  .brand-dot{width:26px;height:26px;border-radius:50%;background:var(--bright-blue);}
  .offers{
    position:absolute;left:70px;top:126px;margin:0;
    font-weight:500;font-size:30px;line-height:32px;color:var(--white);text-transform:uppercase;
  }
  .offers-rule{position:absolute;left:70px;top:236px;width:455px;height:4px;background:var(--white);}
  .headline{
    position:absolute;left:68px;top:254px;margin:0;
    font-weight:800;font-size:59px;line-height:54px;color:var(--heading-navy);letter-spacing:1px;
  }
  .intro{
    position:absolute;left:68px;top:480px;width:800px;margin:0;
    font-size:21.5px;line-height:29.5px;color:var(--body-dark);
  }
  .promise{
    position:absolute;right:43px;top:708px;width:440px;margin:0;text-align:right;
    font-size:18.5px;line-height:26px;color:var(--white);text-transform:uppercase;
  }
  .section-title{
    position:absolute;left:49px;margin:0;
    font-weight:800;font-size:28px;line-height:28px;color:var(--section-navy);
  }
  .section-title.approaches{top:832px;}
  .section-title.partnership{top:1066px;}
  .section-text{
    position:absolute;left:49px;width:880px;margin:0;
    font-size:19.5px;line-height:28.3px;color:var(--body-grey);
  }
  .section-text.approaches{top:923px;}
  .section-text.partnership{top:1102px;}
  .contact-ghost{
    position:absolute;left:110px;top:1335px;margin:0;
    font-family:"Montserrat",sans-serif;font-weight:700;font-size:70px;line-height:1;
    color:rgba(255,255,255,0.06);white-space:nowrap;
  }
  .contact-title{
    position:absolute;left:51px;top:1308px;margin:0;
    font-family:"Montserrat",sans-serif;font-weight:700;font-size:40px;line-height:1;color:var(--white);
  }
  .contact-list{
    position:absolute;left:562px;top:1250px;margin:0;padding:0;list-style:none;
    font-family:"Montserrat",sans-serif;font-weight:700;font-size:23.5px;line-height:36px;color:var(--white);
  }
  .contact-list li{display:flex;align-items:center;gap:8px;}
  .contact-list svg{width:24px;height:24px;flex:none;}
</style>
</head>
<body>
<div class="flyer">
  <svg class="flyer-shapes" viewBox="0 0 985 1390" aria-hidden="false">
    <defs>
      <radialGradient id="heroGlow" cx="0.55" cy="0.45" r="0.55">
        <stop offset="0" stop-color="#8cc6e4" stop-opacity="0.55"/>
        <stop offset="1" stop-color="#5aa6cf" stop-opacity="0"/>
      </radialGradient>
    </defs>
    <rect class="top-band" x="0" y="0" width="985" height="800" fill="var(--navy)"/>
    <path class="hero-field" fill="var(--hero-blue)"
      d="M0,120 C150,30 340,20 520,90 C680,150 800,215 985,120 L985,680 C800,640 650,685 480,745 C320,800 150,800 0,715 Z"/>
    <path class="hero-photo" role="img" aria-label="Soft blurred photo of a raised child's hand reaching upward"
      fill="url(#heroGlow)"
      d="M300,160 C500,140 760,200 780,380 C800,560 620,760 420,760 C260,760 200,560 220,380 C230,260 250,170 300,160 Z"/>
    <path class="wave-navy" fill="var(--navy)"
      d="M0,715 C150,800 320,800 480,745 C650,685 800,640 985,680 L985,720 C800,675 640,720 480,770 C320,820 140,815 0,775 Z"/>
    <path class="wave-bright" fill="var(--bright-blue)"
      d="M360,795 C540,740 780,668 985,712 L985,848 C880,900 720,905 600,872 C520,850 440,815 360,795 Z"/>
    <path class="wave-bright-left" fill="var(--bright-blue)" d="M0,760 L0,782 L30,778 Z"/>
    <path class="footer-band" fill="var(--footer-navy)"
      d="M0,1228 C120,1268 240,1292 420,1270 C620,1240 800,1180 985,1230 L985,1390 L0,1390 Z"/>
  </svg>

  <div class="brand"><span class="brand-dot"></span><span>KESTREL TUITION</span></div>

  <p class="offers">Free Trial<br>Free Consultation,<br>Free Assessment,</p>
  <div class="offers-rule"></div>

  <h1 class="headline">PERSONALISED<br>LEARNING<br>PLANS TO SUIT<br>EVERY CHILD</h1>

  <p class="intro">At Kestrel Tuition every child receives an individualised learning &amp; development plan. The plan is based on a variety of assessments which not only identify strengths and weaknesses in their curriculum mastery, but also their preferred learning style. The Learning Plan is a road map detailing what content needs to be learned and<br>also what is the best way of learning.</p>

  <p class="promise">Kestrel Tuition offers high quality tuition, at an affordable price.We believe that every child has the potential for educational excellence, and it is our aim to ensure they realise it.</p>

  <h2 class="section-title approaches">DIFFERENT STUDENTS<br>REQUIRE DIFFERENT<br>APPROACHES TO LEARNING</h2>
  <p class="section-text approaches">Our highly qualified tutors understand that all of us have variations in how we learn things. Creating opportunities for a mix of VAK (Visual, Auditory &amp; Kinaesthetic) learning styles is just one of our strategies we use to ensure pupils learn in ways they are best suited to. Click here to learn more about VAK learning Styles.</p>

  <h2 class="section-title partnership">WORKING IN PARTERSHIP WITH YOUR CHILD'S SCHOOL</h2>
  <p class="section-text partnership">We believe that working together produces optimum outcomes for success. We establish communication links with our pupil's schools in order to assess and monitor their current and ongoing progress. In particular their strengths and<br>weaknesses in different curriculum areas.</p>

  <p class="contact-ghost">CONTACT US</p>
  <h2 class="contact-title">CONTACT US</h2>

  <ul class="contact-list">
    <li>
      <svg viewBox="0 0 24 24"><path fill="var(--icon-blue)" d="M6.6 10.8c1.4 2.8 3.8 5.1 6.6 6.6l2.2-2.2c.3-.3.7-.4 1-.2 1.1.4 2.3.6 3.6.6.6 0 1 .4 1 1V20c0 .6-.4 1-1 1C10.6 21 3 13.4 3 4c0-.6.4-1 1-1h3.5c.6 0 1 .4 1 1 0 1.3.2 2.5.6 3.6.1.3 0 .7-.2 1z"/></svg>
      <span>0800 555 0192</span>
    </li>
    <li>
      <svg viewBox="0 0 24 24"><rect x="7" y="2" width="10" height="20" rx="2" fill="none" stroke="var(--icon-blue)" stroke-width="2"/><circle cx="12" cy="18.5" r="1.2" fill="var(--icon-blue)"/></svg>
      <span>07700 900 418</span>
    </li>
    <li>
      <svg viewBox="0 0 24 24"><rect x="2" y="5" width="20" height="14" fill="var(--icon-blue)"/><path d="M2 5l10 8 10-8" fill="none" stroke="var(--footer-navy)" stroke-width="1.6"/></svg>
      <span>info@KestrelTuition-example.co.uk</span>
    </li>
  </ul>
</div>
</body>
</html>
```